Posters to advertise a jewellery design school

I would like two pieces of artwork designing for our jewellery design school in Kuala Lumpur Malaysia.
60cm by 180cm poster
100cm by 100cm poster

My personal style is ‘perfectly imperfect’ but we wold like to show that we give quality classes in a fun and artistic / creative environment

The posters must contain our logo and you can choose to use as many or as few images as you like to tell the story or even include hand drawn line images.

https://files.mistreloom.net/share/folders/7kQpR2xZ9mWt4LbN__yHc8sDe3JfVa6g?usp=sharing

Please include the following wording on the poster
So you want to be a jewellery designer?

Part time and full-time classes available in:
Silversmithing
Jewellery design and rendering
Stone setting
Gemmology
Enamelling
Computer aided design
60cm by 180cm poster
100cm by 100cm poster

The posters must contain our logo and you can choose to use as many or as few images as you like to tell the story.

Silversmithing
Stone setting
Gemmology
Enamelling
Computer aided design

60cm by 180cm poster
100cm by 100cm poster

Silversmithing
Stone setting
Gemmology
Enamelling
Computer aided design

```html
<!DOCTYPE html>
<html lang="en">
<head>
<meta charset="utf-8">
<title>Mara Quill Jewellery Academy Poster</title>
<link rel="stylesheet" href="https://fonts.googleapis.com/css2?family=Montserrat:wght@200;300;400;500&display=swap">
<style>
  :root {
    --page: #ffffff;
    --mist-light: #f8f8f8;
    --mist-dark: #e6e6e6;
    --plum-top: #360033;
    --plum-bottom: #0b0007;
    --brand-grey: #5a5a5a;
    --heading-white: #ffffff;
    --caption-grey: #c9c3c9;
    --course-orange: #ec6a1c;
    --contact-grey: #a9a3a9;
    --gem-violet: #6a6ab4;
    --gold: #f3bf2c;
  }
  * { box-sizing: border-box; margin: 0; padding: 0; }
  html, body {
    width: 1200px; height: 1200px; overflow: hidden;
    background: var(--page);
    font-family: "Montserrat", sans-serif;
  }
  .poster {
    position: absolute; left: 150px; top: 0;
    width: 900px; height: 1200px; overflow: hidden;
  }
  .poster-backdrop { position: absolute; inset: 0; }
  .brand {
    position: absolute; left: 0; width: 900px; top: 60px;
    text-align: center; color: var(--brand-grey);
  }
  .brand-dot {
    width: 100px; height: 100px; border-radius: 50%;
    background: var(--mist-dark); border: 2px solid #bdbdbd;
    margin: 0 auto 24px;
  }
  .brand-name {
    font-weight: 400; font-size: 36px; letter-spacing: 0.02em; line-height: 1.1;
  }
  .brand-sub {
    font-weight: 400; font-size: 20px; letter-spacing: 0.12em; margin-top: 6px;
  }
  .headline {
    position: absolute; left: 0; width: 900px; top: 378px;
    text-align: center; color: var(--heading-white);
  }
  .headline-lead {
    font-weight: 200; font-size: 32px; letter-spacing: 0.14em; line-height: 42px;
  }
  .headline-main {
    font-weight: 400; font-size: 28px; letter-spacing: 0.98em; line-height: 42px;
    margin-top: 8px; padding-left: 0.98em;
  }
  .ring-art {
    position: absolute; left: 202px; top: 490px;
    width: 496px; height: 360px; border-radius: 12px;
    background: linear-gradient(180deg, var(--gem-violet) 0%, #8f88c4 45%, var(--gold) 100%);
  }
  .courses {
    position: absolute; left: 0; width: 900px; top: 945px;
    text-align: center;
  }
  .courses-intro {
    color: var(--caption-grey); font-weight: 300; font-size: 14px;
    letter-spacing: 0.12em; line-height: 17px;
  }
  .course-list {
    list-style: none; margin-top: 14px;
    color: var(--course-orange); font-weight: 500; font-size: 24px;
    letter-spacing: 0.16em; line-height: 28px;
  }
  .contact {
    position: absolute; left: 0; width: 900px; top: 1147px;
    text-align: center; color: var(--contact-grey);
    font-weight: 300; font-size: 14px; letter-spacing: 0.05em; line-height: 22px;
  }
</style>
</head>
<body>
<main class="poster">
  <svg class="poster-backdrop" width="900" height="1200" viewBox="0 0 900 1200" aria-hidden="true">
    <defs>
      <linearGradient id="plum" x1="0" y1="0" x2="0" y2="1">
        <stop offset="0" stop-color="var(--plum-top)"/>
        <stop offset="1" stop-color="var(--plum-bottom)"/>
      </linearGradient>
      <radialGradient id="mist" cx="0.5" cy="0.35" r="0.7">
        <stop offset="0" stop-color="var(--mist-light)"/>
        <stop offset="1" stop-color="var(--mist-dark)"/>
      </radialGradient>
    </defs>
    <rect width="900" height="1200" fill="url(#plum)"/>
    <path d="M0 0 H900 V292 Q450 330 0 292 Z" fill="var(--mist-light)"/>
    <path d="M0 0 H900 V210 Q450 320 0 210 Z" fill="url(#mist)"/>
  </svg>

  <header class="brand">
    <div class="brand-dot"></div>
    <p class="brand-name">MARA QUILL</p>
    <p class="brand-sub">jewellery</p>
  </header>

  <h1 class="headline">
    <span class="headline-lead" style="display:block">SO YOU WANT TO BE A</span>
    <span class="headline-main" style="display:block">JEWELLERY DESIGNER?</span>
  </h1>

  <div class="ring-art" role="img" aria-label="Illustration of a gold ring set with a large sparkling violet gemstone"></div>

  <section class="courses">
    <p class="courses-intro">PART TIME AND FULL-TIME CLASSES<br>AVAILABLE IN:</p>
    <ul class="course-list">
      <li>Silversmithing | Stone setting</li>
      <li>Jewellery design and rendering</li>
      <li>Gemmology | Enamelling</li>
      <li>Computer aided design</li>
    </ul>
  </section>

  <footer class="contact">
    <p>Email: academy@maraquilljewellery.com &nbsp;|&nbsp; Phone : +60 10555 0142</p>
    <p>Address : 12B, Lorong Serai, Bangsar, Kuala Lumpur 59100, Malaysia</p>
  </footer>
</main>
</body>
</html>
```